Book Cover

Book Title: THE QUIET LEDGER
Book Sub Title: Notes on slowing the daily rush and shaping a calmer household rhythm
Vibe: Professional, stylish, trustworthy (high-end men's fashion)
Website (for inspiration): www.brindlequarry.com
Attached: a potential photo to use for the cover, but open to other options (from our website)

```html
<!DOCTYPE html>
<html lang="en">
<head>
<meta charset="UTF-8">
<title>The Quiet Ledger — Book Cover</title>
<link href="https://fonts.googleapis.com/css2?family=Instrument+Serif&family=Montserrat:wght@400;500&display=swap" rel="stylesheet">
<style>
  :root {
    --backdrop: #d2b4ac;
    --cover-dark: #5f4035;
    --cover-mid: #6e4a3c;
    --glow: #b9683a;
    --accent: #f08a5d;
    --accent-light: #fde1d2;
    --band: #b8714b;
    --ink-light: #ffffff;
  }
  * { margin: 0; padding: 0; box-sizing: border-box; }
  html, body {
    width: 1105px;
    height: 1200px;
    overflow: hidden;
    background: var(--backdrop);
  }
  .cover {
    position: absolute;
    left: 162px;
    top: 45px;
    width: 780px;
    height: 1110px;
    overflow: hidden;
    background:
      radial-gradient(ellipse 42% 55% at 34% 52%, rgba(185,104,58,0.85), rgba(185,104,58,0) 70%),
      linear-gradient(90deg, var(--cover-mid) 0%, var(--cover-dark) 100%);
    box-shadow: 0 20px 50px rgba(60,35,28,0.35);
  }
  .title {
    position: absolute;
    right: 40px;
    top: 62px;
    text-align: right;
    font-family: "Instrument Serif", serif;
    line-height: 0.82;
  }
  .title-lead {
    display: block;
    font-size: 150px;
    color: var(--ink-light);
    letter-spacing: -2px;
  }
  .title-main {
    display: block;
    font-size: 196px;
    letter-spacing: -3px;
    background: linear-gradient(180deg, var(--accent) 0%, var(--accent-light) 55%, var(--accent) 100%);
    -webkit-background-clip: text;
    background-clip: text;
    color: transparent;
  }
  .portrait {
    position: absolute;
    left: 70px;
    top: 360px;
    width: 340px;
    height: 720px;
    border-radius: 160px 160px 20px 20px;
    background: linear-gradient(180deg, rgba(40,40,60,0.55) 0%, rgba(30,32,55,0.6) 60%, rgba(110,70,45,0.35) 100%);
  }
  .subtitle {
    position: absolute;
    right: 34px;
    top: 395px;
    text-align: right;
    font-family: "Instrument Serif", serif;
    font-size: 66px;
    line-height: 0.86;
    color: var(--ink-light);
    text-transform: uppercase;
  }
  .author-band {
    position: absolute;
    left: 420px;
    right: 0;
    top: 880px;
    height: 105px;
    background: var(--band);
    display: flex;
    flex-direction: column;
    justify-content: center;
    align-items: flex-end;
    padding-right: 50px;
    font-family: "Montserrat", sans-serif;
    font-weight: 500;
    font-size: 22px;
    letter-spacing: 14px;
    line-height: 1.55;
    color: var(--ink-light);
  }
</style>
</head>
<body>
  <main class="cover">
    <h1 class="title">
      <span class="title-lead">THE QUIET</span>
      <span class="title-main">LEDGER</span>
    </h1>
    <div class="portrait" role="img" aria-label="Photograph of the author in a navy suit seated on a wooden bar stool"></div>
    <p class="subtitle">Notes on<br>slowing the<br>daily rush &amp;<br>shaping a<br>calmer<br>household<br>rhythm</p>
    <div class="author-band">
      <span>AUTHOR</span>
      <span>NAME</span>
    </div>
  </main>
</body>
</html>
```